10 Page Marketing Report Template - Quillmont Care Associates

https://www.vexaclip.com/view/8f1d2e7b90c44a6f81e2d3b5c7a9f014

We are creating a professional, modern, and slightly edgy PDF-style report document (about 10 pages) to showcase the results of a client’s first 30 days with Quillmont Care Associates.

The report will be designed as a customizable Canva template so the Client Success team can easily update logos, screenshots, and text for each client.

This document will serve as both a visual presentation piece and a report deliverable, blending clean design, modern layout, and data-driven storytelling.

I am attaching the content for the report doc and the design brief along with the logo.
Here is our website for design style, look, and feel: https://quillmontcare.example/

Here is a quick overview video I made:

```html
<!DOCTYPE html>
<html lang="en">
<head>
<meta charset="utf-8">
<title>30 Days to Value Report — Quillmont Care Associates</title>
<link rel="stylesheet" href="https://fonts.googleapis.com/css2?family=Poppins:wght@400;500;600;700;800;900&display=swap">
<style>
:root{
  --stage:#8e8e8e;
  --navy:#0b1030;
  --blue:#4a9be8;
  --blue-deep:#2f7fd0;
  --ink:#1c1c22;
  --muted:#55575e;
  --paper:#f5f6f9;
  --fade:#3e3e41;
  --white:#ffffff;
}
*{box-sizing:border-box;margin:0;padding:0}
html,body{width:1200px;height:3565px;overflow:hidden}
body{background:var(--stage);font-family:"Poppins",sans-serif;color:var(--ink);position:relative}
.page{position:absolute;width:521px;height:676px;overflow:hidden;
  background:linear-gradient(180deg,var(--paper) 0%,var(--paper) 55%,#cfd0d3 78%,var(--fade) 100%)}
.page.plain{background:var(--white)}
.col-l{left:71px}.col-r{left:610px}
.row1{top:60px}.row2{top:754px}.row3{top:1448px}.row4{top:2141px}.row5{top:2833px}

.run-head{position:absolute;left:0;top:0;width:100%;height:46px}
.run-head .brand{position:absolute;left:18px;top:12px;display:flex;align-items:center;gap:5px}
.brand-square{width:12px;height:12px;background:var(--blue);flex:none}
.brand-name{font-weight:600;font-size:7px;line-height:1.1;color:var(--navy);width:74px}
.run-head .progress{position:absolute;right:20px;top:32px;font-size:7.5px;color:var(--ink)}
.run-head .rule{position:absolute;left:18px;right:18px;top:44px;height:1px;background:var(--blue)}

.title{position:absolute;left:55px;top:70px;font-weight:900;font-size:26px;line-height:1.25;color:var(--blue);text-transform:uppercase;letter-spacing:.2px}
.body{font-size:9px;line-height:1.5;color:var(--ink)}
.label{font-weight:700;font-size:8.5px;text-transform:uppercase;color:var(--ink)}
.bullets{list-style:none}
.bullets li{position:relative;padding-left:14px;font-size:8.8px;line-height:1.4;margin-bottom:12px}
.bullets li::before{content:"";position:absolute;left:0;top:4px;width:6px;height:6px;border-radius:50%;background:var(--ink)}
.abs{position:absolute}

.cover{background:var(--navy)}
.cover .client-logo{position:absolute;left:48px;top:28px;width:219px;height:86px;background:var(--white);display:flex;align-items:center;justify-content:center;font-size:9px;font-weight:500}
.cover .hero{position:absolute;left:48px;top:200px;font-weight:900;font-size:86px;line-height:.86;color:var(--blue);letter-spacing:-2px}
.cover .vertical{position:absolute;left:442px;top:336px;transform:rotate(-90deg);transform-origin:left top;font-weight:900;font-size:34px;color:var(--white);line-height:1}
.cover .sub{position:absolute;left:64px;top:345px;font-weight:800;font-style:italic;font-size:24px;color:var(--white);border-top:2px solid var(--white);padding-top:2px}
.cover .meta{position:absolute;left:50px;top:401px;width:244px;height:36px;background:var(--white);font-size:7px;padding:5px 6px;line-height:1.5}
.cover .mini-logo{position:absolute;left:50px;top:447px;width:80px;height:50px;background:var(--white);display:flex;align-items:center;gap:3px;padding:4px}
.cover .prepared{position:absolute;left:50px;top:505px;font-size:7px;color:var(--white);line-height:1.4}
.cover .prepared b{color:var(--blue);font-weight:700}

.tile{position:absolute;width:127px;height:180px;background:var(--blue);box-shadow:6px 8px 10px rgba(0,0,0,.35);color:var(--white);font-size:8.5px;line-height:1.45;padding:0 16px}
.tile svg{display:block;margin:24px auto 20px}

.funnel{position:absolute;height:48px;background:var(--blue);clip-path:polygon(0 0,100% 0,94% 100%,6% 100%);text-align:center;font-size:8px;line-height:1.35;color:var(--ink);padding-top:8px}
.funnel b{font-weight:700;display:block}

.box{position:absolute;border:1px solid var(--ink);background:var(--white);padding:10px 14px}
.box .label{margin-bottom:12px}
.icon-label{position:absolute;font-size:7.5px;font-weight:600;color:var(--ink)}
</style>
</head>
<body>

<section class="page cover col-l row1">
  <div class="client-logo">Client Logo</div>
  <div class="hero">30 DAYS<br>TO VALUE</div>
  <div class="vertical">REPORT</div>
  <div class="sub">Your First Month of Progress</div>
  <div class="meta">CLIENT: [Client Name]<br>DATE: [Month / Year]</div>
  <div class="mini-logo"><span class="brand-square"></span><span class="brand-name" style="font-size:6px;width:60px">Quillmont Care Associates</span></div>
  <div class="prepared"><b>PREPARED BY:</b><br>Quillmont Care Associates</div>
</section>

<section class="page plain col-r row1">
  <header class="run-head"><div class="brand"><span class="brand-square"></span><span class="brand-name">Quillmont Care Associates</span></div><span class="progress">Day 1–30 progress</span><span class="rule"></span></header>
  <h1 class="title">Welcome &amp;<br>Overview Page</h1>
  <div class="abs body" style="left:55px;top:148px;width:275px">
    <p>The first 30 days are about creating momentum. Our goal was to build the foundation for measurable growth — from your website and Localio Business Profile to your SEO systems, audits, and backlink strategy.</p>
    <p style="margin-top:10px">This report highlights what’s been accomplished and what’s next in your marketing journey.</p>
  </div>
  <svg class="abs" style="left:0;top:0" width="521" height="676" role="img" aria-label="Photo of two business people shaking hands over a café table">
    <defs><linearGradient id="shake" x1="0" y1="0" x2="1" y2="1"><stop offset="0" stop-color="#5d4a3a"/><stop offset=".5" stop-color="#a88a6c"/><stop offset="1" stop-color="#2d3442"/></linearGradient></defs>
    <path d="M0 305 Q330 300 521 150 L521 676 L0 676 Z" fill="url(#shake)"/>
    <path d="M0 305 Q330 300 521 150" fill="none" stroke="var(--blue)" stroke-width="5"/>
  </svg>
</section>

<section class="page col-l row2">
  <header class="run-head"><div class="brand"><span class="brand-square"></span><span class="brand-name">Quillmont Care Associates</span></div><span class="progress">Day 1–30 progress</span><span class="rule"></span></header>
  <h1 class="title">Highlights &amp;<br>Quick Wins</h1>
  <div class="tile" style="left:58px;top:190px"><svg width="40" height="40" viewBox="0 0 40 40"><path d="M28 6 C20 8 14 16 12 24 L16 28 C24 26 32 20 34 12 Z M12 24 L6 22 L12 16 Z M16 28 L18 34 L24 28 Z" fill="#111"/></svg>Website launched and optimized for SEO</div>
  <div class="tile" style="left:202px;top:190px"><svg width="40" height="40" viewBox="0 0 40 40"><path d="M20 4 C12 4 8 10 8 16 C8 25 20 38 20 38 C20 38 32 25 32 16 C32 10 28 4 20 4 Z" fill="#111"/><circle cx="20" cy="16" r="5" fill="var(--blue)"/></svg>Localio Business Profiles verified and optimized</div>
  <div class="tile" style="left:345px;top:190px"><svg width="40" height="40" viewBox="0 0 40 40"><path d="M8 32 L10 24 L28 6 L34 12 L16 30 Z" fill="#111"/></svg>Comprehensive SEO audits completed</div>
  <div class="tile" style="left:58px;top:394px"><svg width="40" height="40" viewBox="0 0 40 40" fill="none" stroke="#111" stroke-width="4"><rect x="6" y="18" width="18" height="10" rx="5" transform="rotate(-45 15 23)"/><rect x="16" y="10" width="18" height="10" rx="5" transform="rotate(-45 25 15)"/></svg>Backlink strategy implementation underway</div>
  <div class="tile" style="left:202px;top:394px"><svg width="40" height="40" viewBox="0 0 40 40" fill="none" stroke="#111" stroke-width="3"><rect x="6" y="10" width="24" height="24" rx="2"/><path d="M11 18h14M11 24h14M11 30h8M24 20 L34 6"/></svg>First blog articles published</div>
  <div class="tile" style="left:345px;top:394px"><svg width="40" height="40" viewBox="0 0 40 40" fill="none" stroke="#111" stroke-width="3"><rect x="6" y="8" width="22" height="28" rx="2"/><path d="M11 28v-6M16 28v-10M21 28v-4"/><circle cx="28" cy="24" r="6"/><path d="M32 28l5 5"/></svg>Tracking and analytics systems connected</div>
</section>

<section class="page col-r row2">
  <header class="run-head"><div class="brand"><span class="brand-square"></span><span class="brand-name">Quillmont Care Associates</span></div><span class="progress">Day 1–30 progress</span><span class="rule"></span></header>
  <h1 class="title" style="font-size:24px">Comprehensive Audits<br>&amp; Strategy Development</h1>
  <p class="abs body" style="left:55px;top:150px;width:400px">To ensure long-term results, our team conducted a full suite of technical and strategic audits during the first month. These insights guided your SEO roadmap and content strategy moving forward.</p>
  <div class="abs" style="left:0;width:100%;top:230px;text-align:center;font-weight:800;font-size:13px">Audits &amp; Deliverables Completed:</div>
  <div class="funnel" style="left:55px;width:411px;top:273px"><b>TECHNICAL SEO AUDIT:</b>Site health, indexation, and crawl efficiency</div>
  <div class="funnel" style="left:82px;width:357px;top:337px"><b>BACKLINK AUDIT:</b>Link quality, toxicity review, and<br>authority scoring</div>
  <div class="funnel" style="left:107px;width:307px;top:401px"><b>COMPETITOR ANALYSIS:</b>Top-ranking competitors’ content,<br>backlinks, and keyword profiles</div>
  <div class="funnel" style="left:130px;width:261px;top:465px"><b>ON-PAGE SEO AUDIT:</b>Metadata, headings, internal links,<br>and content structure</div>
  <div class="funnel" style="left:154px;width:213px;top:529px"><b>CONTENT AUDIT:</b>Keyword targeting, topical gaps,<br>and conversion opportunities</div>
  <div class="funnel" style="left:177px;width:167px;top:593px"><b>STRATEGY DEVELOPMENT:</b>90-day SEO plan and keyword<br>roadmap created</div>
</section>

<section class="page col-l row3">
  <header class="run-head"><div class="brand"><span class="brand-square"></span><span class="brand-name">Quillmont Care Associates</span></div><span class="progress">Day 1–30 progress</span><span class="rule"></span></header>
  <h1 class="title">Website<br>Progress</h1>
  <div class="abs" role="img" aria-label="Laptop and phone mockup showing the new website" style="left:55px;top:152px;width:370px;height:222px;background:linear-gradient(160deg,#2a2f3c 0%,#6f7584 60%,#b7bbc3 100%);border-radius:6px"></div>
  <div class="abs label" style="left:55px;top:398px">Optimizations completed:</div>
  <ul class="abs bullets" style="left:55px;top:420px">
    <li>On-page SEO (titles, meta, H1s)</li><li>Local schema added</li><li>Call tracking integrated</li><li>Mobile responsiveness reviewed</li>
  </ul>
  <div class="abs label" style="left:55px;top:540px">Next steps:</div>
  <ul class="abs bullets" style="left:55px;top:563px">
    <li>CRO improvements</li><li>Additional service or location pages</li>
  </ul>
</section>

<section class="page col-r row3">
  <header class="run-head"><div class="brand"><span class="brand-square"></span><span class="brand-name">Quillmont Care Associates</span></div><span class="progress">Day 1–30 progress</span><span class="rule"></span></header>
  <h1 class="title">Localio Business<br>Profile</h1>
  <ul class="abs bullets" style="left:55px;top:160px">
    <li>Profiles verified and optimized</li><li>Categories, services, and photos updated</li><li>Images updated and optimized for visibility and engagement</li><li>Review strategy initiated</li><li>Visibility and engagement tracking started</li>
  </ul>
  <div class="abs" role="img" aria-label="Faint world map backdrop" style="left:20px;top:310px;width:480px;height:210px;background:radial-gradient(ellipse at center,#c9cace 0%,rgba(201,202,206,0) 70%)"></div>
  <div class="abs" style="left:58px;top:385px;width:367px;height:172px;background:var(--white);box-shadow:0 2px 6px rgba(0,0,0,.25);padding:8px 10px;font-size:6.5px;color:var(--muted)">
    <div style="color:var(--ink);font-size:7px">Customer actions</div>
    <div>The most common actions customers take on your listing</div>
    <div style="margin-top:6px;color:var(--ink)">1 month ▾</div>
    <div style="margin-top:6px;color:var(--ink)">Total actions 69</div>
    <svg class="abs" style="left:14px;top:60px" width="250" height="98" viewBox="0 0 250 98">
      <path d="M0 88H250" stroke="#ccc"/>
      <path d="M0 88 L20 70 L40 84 L60 76 L80 88 L95 60 L115 86 L128 20 L140 84 L160 70 L180 86 L200 72 L220 80 L250 88 Z" fill="#d9e8a8" stroke="#8cbf3f"/>
      <path d="M0 88 L30 78 L55 86 L90 74 L120 86 L150 66 L175 88 L210 80 L250 86" fill="none" stroke="#f2c94c"/>
      <path d="M0 88 L40 82 L80 86 L130 76 L170 84 L230 78 L250 88" fill="none" stroke="#5b8def"/>
      <text x="12" y="97" font-size="5" fill="#777">Feb 21</text><text x="80" y="97" font-size="5" fill="#777">Feb 28</text><text x="150" y="97" font-size="5" fill="#777">Mar 7</text><text x="220" y="97" font-size="5" fill="#777">Mar 14</text>
    </svg>
    <div class="abs" style="left:275px;top:68px;line-height:2.3">
      <div><span style="display:inline-block;width:5px;height:5px;background:#8cbf3f"></span> Visit your website</div>
      <div><span style="display:inline-block;width:5px;height:5px;background:#a7c84c"></span> Request directions</div>
      <div><span style="display:inline-block;width:5px;height:5px;background:#5b8def"></span> Call you</div>
      <div><span style="display:inline-block;width:5px;height:5px;background:#f2c94c"></span> Message you</div>
    </div>
  </div>
  <div class="abs" style="left:58px;top:566px;font-size:8px">LBP performance graph</div>
</section>

<section class="page col-l row4">
  <header class="run-head"><div class="brand"><span class="brand-square"></span><span class="brand-name">Quillmont Care Associates</span></div><span class="progress">Day 1–30 progress</span><span class="rule"></span></header>
  <h1 class="title" style="top:62px">Content &amp; SEO</h1>
  <div class="abs label" style="left:55px;top:120px">SEO progress:</div>
  <ul class="abs bullets" style="left:55px;top:142px;width:340px">
    <li>Initial keyword tracking launched</li><li>On-page SEO and internal linking completed</li><li>Foundational ranking movement observed (if applicable)</li><li>Pillar &amp; Cluster Content Calendar created — outlining key topics, publishing cadence, and interlinking structure for long-term SEO growth</li>
  </ul>
  <svg class="abs" style="left:75px;top:285px" width="360" height="50" viewBox="0 0 360 50" fill="none" stroke="var(--blue)" stroke-width="2">
    <rect x="6" y="4" width="30" height="40" rx="2"/><path d="M12 14h18M12 22h18M12 30h12"/>
    <circle cx="110" cy="10" r="4"/><path d="M102 40l8-8m0 8l-8-8M120 10l10 28"/>
    <circle cx="220" cy="24" r="14"/><circle cx="220" cy="24" r="5"/>
    <path d="M320 44V8m0 0l-8 8m8-8l8 8M310 44l10-14 10 14"/>
  </svg>
  <div class="abs" style="left:55px;top:344px;font-weight:700;font-size:14px">Planning → Strategy → Implementation → Growth</div>
  <div class="abs label" style="left:55px;top:400px">Next steps:</div>
  <ul class="abs bullets" style="left:55px;top:422px">
    <li>Continue publishing cluster blogs weekly</li><li>Begin interlinking to new service pages</li>
  </ul>
  <div class="box" style="left:33px;top:534px;width:454px;height:113px"><div class="label">Blog titles</div><div class="body" style="font-size:8.5px">[List blog titles or link URLs here.]</div></div>
</section>

<section class="page col-r row4">
  <header class="run-head"><div class="brand"><span class="brand-square"></span><span class="brand-name">Quillmont Care Associates</span></div><span class="progress">Day 1–30 progress</span><span class="rule"></span></header>
  <h1 class="title">Citation Listings &amp;<br>Backlink Strategy</h1>
  <div class="box" style="left:42px;top:144px;width:454px;height:113px"><div class="label">Content published:</div><div class="body" style="font-size:8.5px">[List blog titles or link URLs here.]</div></div>
  <div class="abs label" style="left:55px;top:286px">Citation listings:</div>
  <ul class="abs bullets" style="left:55px;top:308px;width:420px">
    <li>Core directories completed (Localio, Findr, Orchard Maps, Reviewly, etc.)</li><li>Industry-specific and regional listings submitted</li><li>NAP (Name–Address–Phone) consistency audit completed</li>
  </ul>
  <div class="abs label" style="left:55px;top:398px">Backlink work:</div>
  <ul class="abs bullets" style="left:55px;top:420px;width:225px">
    <li>Foundational backlinks placed</li><li>Tier-1 authority outreach plan initiated</li><li>Competitor link gap opportunities identified</li>
  </ul>
  <div class="abs label" style="left:55px;top:530px">Next steps:</div>
  <ul class="abs bullets" style="left:55px;top:552px">
    <li>Continue monthly citation expansion</li><li>Launch next wave of backlink outreach</li>
  </ul>
  <div class="abs" role="img" aria-label="Illustration of a globe linked to globe, directory and link icons" style="left:285px;top:395px;width:210px;height:210px;background:linear-gradient(160deg,#d6e6f7 0%,#9cc6ef 100%)"></div>
  <div class="icon-label" style="left:307px;top:401px">Globe</div>
  <div class="icon-label" style="left:392px;top:380px">Directory</div>
  <div class="icon-label" style="left:292px;top:608px">Link</div>
  <div class="abs" style="right:28px;top:636px;font-size:7px;font-weight:600">CORE LISTINGS, &nbsp;AUTHORITY LINKS, TIER 1 OUTREACH</div>
</section>

<section class="page col-l row5">
  <header class="run-head"><div class="brand"><span class="brand-square"></span><span class="brand-name">Quillmont Care Associates</span></div><span class="progress">Day 1–30 progress</span><span class="rule"></span></header>
  <h1 class="title">Tracking &amp;<br>Reporting</h1>
  <ul class="abs bullets" style="left:55px;top:158px">
    <li>Metrica 4 and Indexa Console connected</li><li>Call tracking and form submissions live</li><li>Conversion goals configured</li><li>Dashboard access shared</li>
  </ul>
  <svg class="abs" style="left:302px;top:161px" width="182" height="192" viewBox="0 0 182 192">
    <rect x=".5" y=".5" width="181" height="191" fill="#fff" stroke="#9cc4ee"/>
    <g font-size="6.5" fill="#333">
      <text x="6" y="17">50</text><text x="6" y="42">40</text><text x="6" y="68">30</text><text x="6" y="93">20</text><text x="6" y="119">10</text><text x="10" y="145">0</text>
      <text x="30" y="160">A grade</text><text x="70" y="160">B grade</text><text x="108" y="160">C grade</text><text x="146" y="160">D grade</text>
    </g>
    <g stroke="#ddd"><path d="M22 15H176M22 40H176M22 66H176M22 91H176M22 117H176"/></g>
    <path d="M22 143H176" stroke="#888"/>
    <g>
      <rect x="34" y="107" width="7" height="36" fill="#4472c4"/><rect x="41" y="84" width="7" height="59" fill="#c0504d"/><rect x="48" y="79" width="7" height="64" fill="#9bbb59"/>
      <rect x="72" y="74" width="7" height="69" fill="#4472c4"/><rect x="79" y="38" width="7" height="105" fill="#c0504d"/><rect x="86" y="86" width="7" height="57" fill="#9bbb59"/>
      <rect x="110" y="40" width="7" height="103" fill="#4472c4"/><rect x="117" y="71" width="7" height="72" fill="#c0504d"/><rect x="124" y="79" width="7" height="64" fill="#9bbb59"/>
      <rect x="148" y="99" width="7" height="44" fill="#4472c4"/><rect x="155" y="112" width="7" height="31" fill="#c0504d"/><rect x="162" y="132" width="7" height="11" fill="#9bbb59"/>
    </g>
  </svg>
  <div class="abs" style="left:302px;top:362px;font-size:8.5px;line-height:1.9">☼ Data<br>▮ Charts<br>▤ Dashboards</div>
  <div class="abs label" style="left:55px;top:550px">Next steps:</div>
  <ul class="abs bullets" style="left:55px;top:572px">
    <li>Monitor traffic and lead source data</li><li>Review conversion metrics monthly</li>
  </ul>
</section>

<section class="page plain col-r row5">
  <header class="run-head"><div class="brand"><span class="brand-square"></span><span class="brand-name">Quillmont Care Associates</span></div><span class="progress">Day 1–30 progress</span><span class="rule"></span></header>
  <h1 class="title" style="left:46px;top:78px">What’s Next<br>(Days 31–60)</h1>
  <ul class="abs bullets" style="left:46px;top:168px;width:215px">
    <li style="font-size:10px;font-weight:500">Continue backlink outreach and citation expansion</li>
    <li style="font-size:10px;font-weight:500">Publish next wave of blog content</li>
    <li style="font-size:10px;font-weight:500">Drive organic traffic growth via SEO</li>
    <li style="font-size:10px;font-weight:500">Launch paid campaigns (if applicable)</li>
    <li style="font-size:10px;font-weight:500">Review analytics data and optimize for conversions</li>
  </ul>
  <div class="abs" role="img" aria-label="Photo of a businessman climbing stone stairs toward the sky" style="left:274px;top:194px;width:195px;height:235px;background:linear-gradient(180deg,#bcd3ea 0%,#e6edf3 45%,#9a9a96 70%,#5e5e5b 100%)"></div>
  <div class="abs" style="left:42px;top:432px;background:var(--blue);color:var(--white);font-weight:700;font-size:9px;padding:1px 5px">NOTES &amp; RECOMMENDATIONS</div>
  <p class="abs body" style="left:42px;top:458px;width:420px;font-size:8.8px">The foundation is in place. The next phase focuses on growth, visibility, and conversions. We’re excited about the direction and look forward to building on this momentum.</p>
  <div class="abs" style="left:42px;top:537px;width:152px;height:100px;background:var(--white);box-shadow:0 1px 6px rgba(0,0,0,.3);display:flex;align-items:center;justify-content:center;gap:6px">
    <span class="brand-square" style="width:16px;height:16px"></span><span class="brand-name" style="font-size:10px;width:96px">Quillmont Care Associates</span>
  </div>
  <div class="abs" style="left:217px;top:550px;font-weight:700;font-size:9px;text-decoration:underline">PREPARED BY:</div>
  <div class="abs" style="left:217px;top:600px;font-size:10px">Dana Whitcombe</div>
  <div class="abs" style="left:217px;top:615px;font-size:7px;color:var(--muted)">Head of Client Success | Quillmont Care Associates</div>
</section>

</body>
</html>
```